Paws Home

Need Yard signs
Dimensions 24" wide and 18" high

Copy: Rescue does not mean "Damaged". It means they have been let down by humans.
Please adopt at: 217 W Brannock Ave, Tampa, Fl 33682
Open: Tues-Sun 10am - 7pm

I have attached a sample of the original ad. I can't use this because the resolution is too low and the type has to be big enough so that it can be seen 12 feet away.
I have also attached some photos you can use. The res may not be hi enough, but perhaps you can find some stock photography even these pics are not hi res enough.

Target Market(s)

animal lovers

Font styles to use
Sans Serif

Colors

Designer to choose colors to be used in the design.

Requirements
Must have
• Must be easy to read.

```html
<!DOCTYPE html>
<html lang="en">
<head>
<meta charset="utf-8">
<title>Paws Home – Yard Sign</title>
<link rel="stylesheet" href="https://fonts.googleapis.com/css2?family=Didact+Gothic&family=Montserrat:wght@800&family=Jost:wght@600&display=swap">
<style>
  :root {
    --paper: #ffffff;
    --green: #8cc63f;
    --navy: #0b1070;
    --ink-grey: #555558;
    --frame: #2b3266;
    --photo-tan: #b59a7c;
    --photo-teal: #4f8a86;
    --photo-grey: #c9c6c0;
  }
  html, body {
    margin: 0;
    padding: 0;
    width: 1200px;
    height: 889px;
    overflow: hidden;
    background: var(--paper);
  }
  .sign {
    position: relative;
    width: 1200px;
    height: 889px;
    background: var(--paper);
    overflow: hidden;
  }
  .hero-photo {
    position: absolute;
    left: 0;
    top: 0;
    width: 1200px;
    height: 440px;
  }
  .message-box {
    position: absolute;
    left: 150px;
    top: 469px;
    width: 899px;
    height: 286px;
    border: 2px solid var(--frame);
    box-sizing: border-box;
    box-shadow: 0 16px 14px -10px rgba(0,0,0,0.22);
    background: var(--paper);
    text-align: center;
  }
  .kicker {
    position: absolute;
    top: -26px;
    left: 50%;
    transform: translateX(-50%);
    padding: 0 8px;
    background: var(--paper);
    font-family: "Didact Gothic", sans-serif;
    font-size: 42px;
    line-height: 52px;
    color: var(--ink-grey);
    white-space: nowrap;
  }
  .headline {
    margin: 26px 0 0;
    font-family: "Montserrat", sans-serif;
    font-weight: 800;
    font-size: 146px;
    line-height: 150px;
    letter-spacing: -1px;
    color: var(--green);
  }
  .subline {
    margin: 4px 0 0;
    font-family: "Didact Gothic", sans-serif;
    font-size: 42px;
    line-height: 46px;
    color: var(--ink-grey);
  }
  .info-band {
    position: absolute;
    left: 0;
    bottom: 0;
    width: 1200px;
    height: 107px;
    background: var(--navy);
    display: flex;
    align-items: center;
    justify-content: center;
    gap: 14px;
    font-family: "Jost", sans-serif;
    font-weight: 600;
    font-size: 34px;
    color: #ffffff;
    white-space: nowrap;
  }
  .info-item {
    display: flex;
    align-items: center;
    gap: 10px;
  }
  .info-icon { flex: none; }
</style>
</head>
<body>
<main class="sign">
  <svg class="hero-photo" viewBox="0 0 1200 440" role="img" aria-label="Photo of a brindle and white rescue dog looking through a chain-link kennel fence">
    <defs>
      <linearGradient id="photoTones" x1="0" y1="0" x2="1" y2="0">
        <stop offset="0" stop-color="#6f9c98"/>
        <stop offset="0.3" stop-color="#a88a6a"/>
        <stop offset="0.55" stop-color="#b59a7c"/>
        <stop offset="0.8" stop-color="#4f7f7c"/>
        <stop offset="1" stop-color="#d4d0c8"/>
      </linearGradient>
    </defs>
    <path fill="url(#photoTones)" d="M40 0 H1176 L1168 40 L1182 70 L1170 110 L1186 150 L1172 190 L1180 240 L1160 290 L1168 330 L1140 360 L1130 400 L1100 390 L1080 420 L1040 405 L1000 430 L960 410 L900 425 L840 405 L780 420 L720 400 L660 415 L600 398 L540 412 L480 395 L420 410 L360 390 L300 405 L240 385 L180 398 L130 375 L90 380 L75 340 L60 300 L72 260 L48 220 L60 180 L42 140 L58 100 L40 60 Z"/>
  </svg>

  <section class="message-box">
    <span class="kicker">RESCUE DOES NOT MEAN</span>
    <h1 class="headline">DAMAGED</h1>
    <p class="subline">IT MEANS THEY HAVE BEEN LET DOWN<br>BY HUMANS</p>
  </section>

  <footer class="info-band">
    <span class="info-item">
      <svg class="info-icon" width="30" height="30" viewBox="0 0 24 24" aria-hidden="true">
        <rect x="2" y="4" width="18" height="16" rx="2" fill="none" stroke="#8cc63f" stroke-width="2"/>
        <line x1="2" y1="9" x2="20" y2="9" stroke="#8cc63f" stroke-width="2"/>
        <line x1="7" y1="2" x2="7" y2="6" stroke="#8cc63f" stroke-width="2"/>
        <line x1="15" y1="2" x2="15" y2="6" stroke="#8cc63f" stroke-width="2"/>
        <circle cx="18" cy="18" r="5" fill="#0b1070" stroke="#8cc63f" stroke-width="2"/>
        <path d="M18 15.5 V18 H20" fill="none" stroke="#8cc63f" stroke-width="1.6"/>
      </svg>
      Tues-Sun 10am - 7pm
    </span>
    <span class="info-item">
      <svg class="info-icon" width="22" height="30" viewBox="0 0 16 22" aria-hidden="true">
        <path d="M8 1 C4 1 1.5 4 1.5 7.5 C1.5 12 8 21 8 21 C8 21 14.5 12 14.5 7.5 C14.5 4 12 1 8 1 Z" fill="#8cc63f"/>
        <circle cx="8" cy="7.5" r="2.6" fill="#0b1070"/>
      </svg>
      217 W Brannock Ave, Tampa, Fl 33682
    </span>
  </footer>
</main>
</body>
</html>
```